Educational Agency in Abu Dhabi looking for an 8 pages website

We are looking for an 8 pages design for a website, we already have one but we need to refine it and it is www.brightcampuslink.ae - Please base it on logo colours (attached) I have uploaded our logo, website content logo colors to use it for the scheme.
We are looking for a smooth look and content added if possible, I also attached content and logo

Industry/Entity Type

Education

Coding

Coded - Design and coding required

Number of Pages Required

5+ page

```html
<!DOCTYPE html>
<html lang="en">
<head>
<meta charset="utf-8">
<title>Bright Campus – Study Abroad</title>
<link href="https://fonts.googleapis.com/css2?family=Roboto:wght@400;500;700&display=swap" rel="stylesheet">
<style>
:root{
  --navy:#1f3265;
  --navy-dark:#172754;
  --ink:#222;
  --muted:#555;
  --light:#f3f3f3;
  --topbar:#1b1b1b;
  --footer:#151515;
  --white:#fff;
}
*{box-sizing:border-box;margin:0;padding:0}
html,body{width:1200px;height:4489px;overflow:hidden}
body{font-family:'Roboto',Arial,sans-serif;color:var(--ink);background:var(--white);position:relative}
.abs{position:absolute}
.topbar{position:absolute;top:0;left:0;width:1200px;height:36px;background:var(--topbar);color:#fff;font-size:13px}
.topbar .phone{left:120px;top:10px}
.topbar .mail{left:538px;top:10px}
.topbar .social{right:120px;top:8px;display:flex;gap:6px}
.dot{width:20px;height:20px;border-radius:50%;background:var(--navy);display:block}
.header{position:absolute;top:36px;left:0;width:1200px;height:99px;background:#fff}
.burger{left:120px;top:42px;width:26px}
.burger span{display:block;height:3px;background:#222;margin-bottom:5px}
.brand{left:0;width:1200px;top:28px;text-align:center;font-weight:700;font-size:22px;color:var(--navy);letter-spacing:.5px}
.brand small{display:block;font-size:11px;font-weight:500;letter-spacing:3px;margin-top:2px}
.btn-apply{right:120px;top:32px;width:152px;height:34px;border-radius:17px;background:var(--navy);color:#fff;font-size:14px;line-height:34px;text-align:center}
.hero{position:absolute;top:135px;left:0;width:1200px;height:593px;background:linear-gradient(180deg,#d9d3cc 0%,#b89a86 45%,#7b5a46 100%)}
.hero h1{position:absolute;top:290px;left:0;width:1200px;text-align:center;color:#fff;font-size:28px;font-weight:500;line-height:34px;text-shadow:0 1px 3px rgba(0,0,0,.5)}
.arrow{position:absolute;top:240px;width:34px;height:34px;border-radius:50%;background:rgba(0,0,0,.45)}
.stats{position:absolute;top:635px;left:120px;display:flex;gap:12px}
.stat{width:232px;height:208px;background:var(--navy);color:#fff;text-align:center;padding-top:30px;border:2px solid rgba(255,255,255,.25)}
.stat b{display:block;font-size:34px;font-weight:700}
.stat svg{margin:14px 0 10px}
.stat span{display:block;font-size:20px}
.why{position:absolute;top:900px;left:120px}
.why h2{font-size:28px;font-weight:500;margin-bottom:18px}
.why p{width:315px;font-size:13.5px;line-height:19px;color:var(--muted);margin-bottom:14px}
.btn-navy{display:inline-block;background:var(--navy);color:#fff;border-radius:18px;font-size:14px;padding:9px 30px}
.why-photo{position:absolute;top:906px;left:453px;width:301px;height:302px;background:linear-gradient(160deg,#9fc3e4 0%,#4a6488 60%,#2b3040 100%)}
.consult{position:absolute;top:906px;left:780px;width:302px;height:302px;background:var(--navy);padding:14px 18px;color:#fff}
.consult h3{text-align:center;font-size:18px;font-weight:500;margin-bottom:10px}
.field{border-bottom:1px solid rgba(255,255,255,.45);height:38px;font-size:12px;padding-top:12px;padding-left:6px}
.field.tall{height:80px}
.btn-send{margin-top:12px;height:30px;background:#fff;color:var(--navy);border-radius:6px;text-align:center;line-height:30px;font-size:13px}
.band{position:absolute;left:0;width:1200px;background:var(--navy);color:#fff}
.sec-title{position:absolute;left:0;width:1200px;text-align:center;font-size:28px;font-weight:500}
.dest{top:1292px;height:691px}
.dest .sec-title{top:66px}
.viewmore{position:absolute;right:120px;top:88px;font-size:14px;border-bottom:1px solid #fff}
.dest-grid{position:absolute;left:120px;top:126px;display:grid;grid-template-columns:repeat(4,228px);column-gap:18px;row-gap:50px}
.dest-card .pic{width:228px;height:190px}
.dest-card p{text-align:center;font-size:17px;margin-top:10px}
.pic.uk{background:linear-gradient(180deg,#5b3a2a,#1c1b2c)}
.pic.usa{background:linear-gradient(180deg,#8fb9de,#4d7658)}
.pic.aus{background:linear-gradient(180deg,#6aa4d8,#2b5876)}
.pic.eng{background:linear-gradient(135deg,#f0d7b6,#d6a052)}
.pic.nz{background:linear-gradient(180deg,#7fa2c8,#5b6a48)}
.pic.eu{background:linear-gradient(180deg,#8cc2ea,#4a6a82)}
.pic.my{background:linear-gradient(180deg,#4a7bbf,#1c3158)}
.pic.uae{background:linear-gradient(180deg,#9bc6e6,#b8a07c)}
.uk-overlay{position:relative;height:190px;background:rgba(0,0,0,.35);text-align:center;padding-top:58px;font-size:13px}
.dots{position:absolute;left:0;width:1200px;text-align:center;top:646px}
.dots i{display:inline-block;width:7px;height:7px;border-radius:50%;background:rgba(255,255,255,.5);margin:0 3px}
.dots i:first-child{background:#fff}
.features{position:absolute;top:1983px;left:0;width:1200px;height:703px}
.features .sec-title{top:80px;color:var(--ink)}
.feat-grid{position:absolute;left:120px;top:145px;display:grid;grid-template-columns:repeat(3,320px);column-gap:0;row-gap:14px}
.feat{height:250px;text-align:center;padding-top:8px}
.feat.hl{background:var(--light)}
.feat h4{font-size:16px;font-weight:500;margin:14px 0 6px;line-height:20px}
.feat p{font-size:12.5px;line-height:16px;color:var(--muted)}
.feat .more{font-size:12.5px;color:var(--muted);margin-top:8px}
.news{top:2686px;height:694px}
.news .sec-title{top:90px}
.news .sub{position:absolute;top:132px;left:0;width:1200px;text-align:center;font-size:14px}
.news-grid{position:absolute;left:120px;top:188px;display:flex;gap:21px}
.news-card{width:308px;height:327px;background:#fff;color:var(--ink)}
.news-card .pic{height:172px;position:relative}
.nc1{background:linear-gradient(160deg,#c9b9a8,#6d5a4c)}
.nc2{background:linear-gradient(160deg,#9fd0f0,#d9a86e)}
.nc3{background:linear-gradient(160deg,#a7c08c,#5e4e3c)}
.badge{position:absolute;left:10px;top:12px;width:34px;height:40px;background:var(--navy);color:#fff;font-size:12px;text-align:center;padding-top:6px;line-height:13px}
.news-card .body{padding:14px 14px}
.news-card h5{font-size:14px;font-weight:500;margin-bottom:6px}
.meta{font-size:12px;color:var(--muted);display:flex;justify-content:space-between;margin-bottom:8px}
.news-card p{font-size:12px;line-height:16px;color:var(--muted)}
.news-card .rm{font-size:12.5px;margin-top:8px}
.btn-white{position:absolute;left:524px;top:578px;width:154px;height:42px;background:#fff;color:var(--navy);border-radius:21px;text-align:center;line-height:42px;font-size:15px}
.partners{position:absolute;top:3380px;left:0;width:1200px;height:678px}
.partners .sec-title{top:42px;color:var(--ink)}
.p-grid{position:absolute;left:120px;top:108px;display:grid;grid-template-columns:repeat(5,175px);column-gap:14px;row-gap:24px}
.p-cell{height:118px;background:var(--light);display:flex;align-items:center;justify-content:center}
.p-cell span{width:110px;height:42px;background:#c9ccd6;border-radius:4px}
.pdots{position:absolute;top:396px;left:0;width:1200px;text-align:center}
.pdots i{display:inline-block;width:7px;height:7px;border-radius:50%;background:#bbb;margin:0 3px}
.pdots i:first-child{background:#555}
.newsletter h3{position:absolute;top:440px;width:1200px;text-align:center;font-size:28px;font-weight:500}
.newsletter p{position:absolute;top:482px;width:1200px;text-align:center;font-size:14px;color:var(--muted)}
.nl-input{position:absolute;top:536px;left:320px;width:432px;height:42px;background:var(--light);border-radius:21px 0 0 21px;font-size:13px;color:#999;padding:13px 24px}
.nl-btn{position:absolute;top:536px;left:752px;width:144px;height:42px;background:var(--navy);color:#fff;border-radius:0 21px 21px 0;text-align:center;line-height:42px;font-size:15px;font-weight:500}
.footer{position:absolute;top:4058px;left:0;width:1200px;height:368px;background:var(--footer);color:#ddd}
.f-brand{position:absolute;left:100px;top:70px;font-size:24px;font-weight:700;color:#fff;line-height:26px}
.f-about{position:absolute;left:100px;top:130px;width:200px;font-size:12.5px;line-height:17px}
.f-about b{display:block;margin-top:8px;font-weight:500;font-size:12px}
.f-col{position:absolute;top:84px}
.f-col h4{font-size:17px;font-weight:500;color:#fff;margin-bottom:16px}
.f-col li{list-style:none;font-size:12.5px;line-height:20px}
.f-col li::before{content:"• ";}
.contact-item{display:flex;gap:10px;font-size:12.5px;line-height:17px;margin-bottom:10px;width:260px}
.f-form{display:grid;grid-template-columns:110px 110px;gap:8px}
.f-form div{height:24px;background:#2a2a2a;font-size:11px;padding:5px 6px}
.f-form .wide{grid-column:span 2}
.f-form .msg{height:60px}
.f-send{width:90px;height:22px;background:var(--navy);color:#fff;font-size:11px;text-align:center;line-height:22px;margin-top:8px}
.bottombar{position:absolute;top:4426px;left:0;width:1200px;height:63px;background:var(--navy);color:#fff;font-size:12.5px}
.bottombar .copy{position:absolute;left:120px;top:23px}
.bottombar .social{position:absolute;right:120px;top:19px;display:flex;gap:6px}
.bottombar .dot{background:#fff;opacity:.85}
</style>
</head>
<body>

<div class="topbar">
  <span class="abs phone">971 50 000 2468</span>
  <span class="abs mail">info@brightcampuslink.ae</span>
  <div class="abs social"><span class="dot"></span><span class="dot"></span><span class="dot"></span><span class="dot"></span></div>
</div>

<header class="header">
  <div class="abs burger"><span></span><span></span><span></span></div>
  <div class="abs brand">BRIGHT CAMPUS<small>STUDY ABROAD</small></div>
  <div class="abs btn-apply">Apply Now</div>
</header>

<section class="hero" role="img" aria-label="Group of smiling students sitting together with laptops and books">
  <h1>Bright Campus Is The Number One Choice<br>For Students To Study Abroad</h1>
  <span class="arrow" style="left:36px"><svg width="34" height="34"><path d="M20 10l-7 7 7 7" stroke="#fff" stroke-width="2.5" fill="none"/></svg></span>
  <span class="arrow" style="right:36px"><svg width="34" height="34"><path d="M14 10l7 7-7 7" stroke="#fff" stroke-width="2.5" fill="none"/></svg></span>
</section>

<div class="stats">
  <div class="stat"><b>980+</b>
    <svg width="64" height="36" viewBox="0 0 64 36" fill="#fff"><circle cx="32" cy="9" r="8"/><path d="M18 36c0-9 6-14 14-14s14 5 14 14z"/><circle cx="12" cy="13" r="6"/><path d="M0 36c0-7 5-11 12-11 3 0 5 1 7 2-2 3-3 6-3 9z"/><circle cx="52" cy="13" r="6"/><path d="M64 36c0-7-5-11-12-11-3 0-5 1-7 2 2 3 3 6 3 9z"/></svg>
    <span>Students</span></div>
  <div class="stat"><b>150+</b>
    <svg width="40" height="36" viewBox="0 0 40 40" fill="#fff"><path d="M38 4c-2-2-5-1-7 1l-7 7-18-5-4 4 14 9-7 7-5-1-3 3 7 4 4 7 3-3-1-5 7-7 9 14 4-4-5-18 7-7c2-2 3-5 1-7z"/></svg>
    <span>Immigration</span></div>
  <div class="stat"><b>550+</b>
    <svg width="40" height="36" viewBox="0 0 40 36" fill="#fff"><path d="M20 0L2 9h36z"/><rect x="4" y="11" width="32" height="3"/><rect x="7" y="16" width="4" height="13"/><rect x="14" y="16" width="4" height="13"/><rect x="22" y="16" width="4" height="13"/><rect x="29" y="16" width="4" height="13"/><rect x="2" y="31" width="36" height="4"/></svg>
    <span>Universities</span></div>
  <div class="stat"><b>30+</b>
    <svg width="36" height="36" viewBox="0 0 36 36" fill="none" stroke="#fff" stroke-width="2.5"><circle cx="18" cy="18" r="16"/><ellipse cx="18" cy="18" rx="7" ry="16"/><path d="M2 18h32M5 9h26M5 27h26"/></svg>
    <span>Country</span></div>
</div>

<section class="why">
  <h2>Why Bright Campus?</h2>
  <p>BRIGHT CAMPUS Abu Dhabi is one of the leading and fastest growing educational consulting companies based in the UAE, trusted by families and partner institutions for clear, honest guidance at every step.</p>
  <p>Bright Campus was founded with an aim to provide professional consultancy services for the recruitment of quality international students to educational institutions based in UK, USA, Canada, Australia, Malaysia, Germany, Europe, Middle East and many more.</p>
  <span class="btn-navy">Read More</span>
</section>
<div class="why-photo" role="img" aria-label="Graduates throwing caps into the air"></div>
<form class="consult">
  <h3>Free Consultation</h3>
  <div class="field">Full name</div>
  <div class="field">Phone</div>
  <div class="field">Email</div>
  <div class="field tall">Message</div>
  <div class="btn-send">Send</div>
</form>

<section class="band dest">
  <h2 class="sec-title">Study Destinations</h2>
  <span class="viewmore">View More</span>
  <div class="dest-grid">
    <div class="dest-card"><div class="pic uk" role="img" aria-label="City skyline at night in the United Kingdom"><div class="uk-overlay">Bright Campus in UK<br>Lorem Ipsum is simply dummy<br>printing and typesetting.</div></div><p>Study in UK</p></div>
    <div class="dest-card"><div class="pic usa" role="img" aria-label="Landmark statue in the United States"></div><p>Study in USA</p></div>
    <div class="dest-card"><div class="pic aus" role="img" aria-label="Harbour landmark in Australia"></div><p>Study in Australia</p></div>
    <div class="dest-card"><div class="pic eng" role="img" aria-label="Student with English language books"></div><p>Study English Language</p></div>
    <div class="dest-card"><div class="pic nz" role="img" aria-label="Historic building in New Zealand"></div><p>Study in New Zealand</p></div>
    <div class="dest-card"><div class="pic eu" role="img" aria-label="Bridge over a river in Europe"></div><p>Study in Europe</p></div>
    <div class="dest-card"><div class="pic my" role="img" aria-label="City towers at dusk in Malaysia"></div><p>Study in Malaysia</p></div>
    <div class="dest-card"><div class="pic uae" role="img" aria-label="Modern skyline in the United Arab Emirates"></div><p>Study in UAE</p></div>
  </div>
  <div class="dots"><i></i><i></i><i></i></div>
</section>

<section class="features">
  <h2 class="sec-title">Why Bright Campus?</h2>
  <div class="feat-grid">
    <div class="feat"><svg width="66" height="74" viewBox="0 0 66 74"><path d="M33 0l33 18.5v37L33 74 0 55.5v-37z" fill="var(--navy)"/><rect x="21" y="24" width="24" height="26" fill="none" stroke="#fff" stroke-width="2.5"/><path d="M26 30h4M36 30h4M26 37h4M36 37h4M30 50v-6h6v6" stroke="#fff" stroke-width="2.5"/></svg>
      <h4>Equipped Office</h4><p>Lorem Ipsum is simply dummy<br>of the printing and typesetting.</p><div class="more">Read More ⊕</div></div>
    <div class="feat"><svg width="66" height="74" viewBox="0 0 66 74"><path d="M33 0l33 18.5v37L33 74 0 55.5v-37z" fill="var(--navy)"/><path d="M33 22l-14 7h28z" fill="#fff"/><path d="M23 32v14M29 32v14M37 32v14M43 32v14M19 50h28" stroke="#fff" stroke-width="2.5"/></svg>
      <h4>Official tie up with Universities,<br>Institutions, and Schools</h4><p>Lorem Ipsum is simply dummy<br>of the printing and typesetting.</p><div class="more">Read More ⊕</div></div>
    <div class="feat"><svg width="66" height="74" viewBox="0 0 66 74"><path d="M33 0l33 18.5v37L33 74 0 55.5v-37z" fill="var(--navy)"/><circle cx="33" cy="30" r="7" fill="none" stroke="#fff" stroke-width="2.5"/><path d="M20 52c0-8 6-12 13-12s13 4 13 12" fill="none" stroke="#fff" stroke-width="2.5"/></svg>
      <h4>Experienced Counselors</h4><p>Lorem Ipsum is simply dummy<br>of the printing and typesetting.</p><div class="more">Read More ⊕</div></div>
    <div class="feat"><svg width="66" height="74" viewBox="0 0 66 74"><path d="M33 0l33 18.5v37L33 74 0 55.5v-37z" fill="var(--navy)"/><path d="M33 20l12 5v10c0 8-6 13-12 16-6-3-12-8-12-16V25z" fill="none" stroke="#fff" stroke-width="2.5"/><path d="M27 36l4 4 8-8" fill="none" stroke="#fff" stroke-width="2.5"/></svg>
      <h4>Quality of Counseling</h4><p>Lorem Ipsum is simply dummy<br>of the printing and typesetting.</p><div class="more">Read More ⊕</div></div>
    <div class="feat hl"><svg width="66" height="74" viewBox="0 0 66 74"><path d="M33 0l33 18.5v37L33 74 0 55.5v-37z" fill="var(--navy)"/><rect x="22" y="21" width="22" height="30" fill="none" stroke="#fff" stroke-width="2.5"/><path d="M27 29h12M27 35h12M27 41h7" stroke="#fff" stroke-width="2.5"/></svg>
      <h4>Registration / License</h4><p>Lorem Ipsum is simply dummy<br>of the printing and typesetting.</p><div class="more">Read More ⊕</div></div>
    <div class="feat"><svg width="66" height="74" viewBox="0 0 66 74"><path d="M33 0l33 18.5v37L33 74 0 55.5v-37z" fill="var(--navy)"/><circle cx="33" cy="37" r="14" fill="none" stroke="#fff" stroke-width="2.5"/><ellipse cx="33" cy="37" rx="6" ry="14" fill="none" stroke="#fff" stroke-width="2"/><path d="M19 37h28" stroke="#fff" stroke-width="2"/></svg>
      <h4>Range of Countries</h4><p>Lorem Ipsum is simply dummy<br>of the printing and typesetting.</p><div class="more">Read More ⊕</div></div>
  </div>
</section>

<section class="band news">
  <h2 class="sec-title">News &amp; Updates</h2>
  <div class="sub">Lorem Ipsum is simply dummyof the printing typesetting.</div>
  <div class="news-grid">
    <article class="news-card"><div class="pic nc1" role="img" aria-label="Students studying together at a table"><div class="badge">19<br>Oct</div></div><div class="body"><h5>Post Title Heading</h5><div class="meta"><span>▣ October 19, 2018</span><span>◌ 12 &nbsp;◌ 20</span></div><p>Lorem Ipsum is simply in dummy text the printing in matter and typesetting industry.</p><div class="rm">Read More ⊕</div></div></article>
    <article class="news-card"><div class="pic nc2" role="img" aria-label="Student working on a laptop outdoors"><div class="badge">19<br>Oct</div></div><div class="body"><h5>Post Title Heading</h5><div class="meta"><span>▣ October 19, 2018</span><span>◌ 12 &nbsp;◌ 20</span></div><p>Lorem Ipsum is simply in dummy text the printing in matter and typesetting industry.</p><div class="rm">Read More ⊕</div></div></article>
    <article class="news-card"><div class="pic nc3" role="img" aria-label="Group of students sitting on grass with books"><div class="badge">19<br>Oct</div></div><div class="body"><h5>Post Title Heading</h5><div class="meta"><span>▣ October 19, 2018</span><span>◌ 12 &nbsp;◌ 20</span></div><p>Lorem Ipsum is simply in dummy text the printing in matter and typesetting industry.</p><div class="rm">Read More ⊕</div></div></article>
  </div>
  <div class="btn-white">Read More</div>
</section>

<section class="partners">
  <h2 class="sec-title">Our Partners</h2>
  <div class="p-grid">
    <div class="p-cell"><span></span></div><div class="p-cell"><span></span></div><div class="p-cell"><span></span></div><div class="p-cell"><span></span></div><div class="p-cell"><span></span></div>
    <div class="p-cell"><span></span></div><div class="p-cell"><span></span></div><div class="p-cell"><span></span></div><div class="p-cell"><span></span></div><div class="p-cell"><span></span></div>
  </div>
  <div class="pdots"><i></i><i></i><i></i></div>
  <div class="newsletter">
    <h3>Subscribe To Our Newsletter</h3>
    <p>To Receive The Latest News And Update</p>
    <div class="nl-input">Your E-Mail</div>
    <div class="nl-btn">SUBMIT</div>
  </div>
</section>

<footer class="footer">
  <div class="f-brand">BRIGHT<br>CAMPUS</div>
  <div class="f-about">Lorem Ipsum is simply dummy text of the printing and typesetting industry.<b>READ MORE ⊕</b></div>
  <div class="f-col" style="left:354px"><h4>Quick Link</h4><ul><li>Study in UK</li><li>Study in USA</li><li>Study in Australia</li><li>Study in New Zealand</li><li>Study in Europe</li><li>Study in Malaysia</li><li>Study in UAE</li></ul></div>
  <div class="f-col" style="left:564px"><h4>Quick Contact</h4>
    <div class="contact-item"><svg width="12" height="16" viewBox="0 0 12 16"><path d="M6 0a6 6 0 00-6 6c0 4.5 6 10 6 10s6-5.5 6-10a6 6 0 00-6-6zm0 8.5A2.5 2.5 0 116 3.5a2.5 2.5 0 010 5z" fill="#ddd"/></svg><span>Harbour View Tower<br>12th floor, Office 1204<br>PO Box 4410</span></div>
    <div class="contact-item"><svg width="14" height="14" viewBox="0 0 24 24"><path d="M6.6 10.8a15 15 0 006.6 6.6l2.2-2.2c.3-.3.7-.4 1-.2 1.1.4 2.3.6 3.6.6.6 0 1 .4 1 1V20c0 .6-.4 1-1 1A17 17 0 013 4c0-.6.4-1 1-1h3.5c.6 0 1 .4 1 1 0 1.3.2 2.5.6 3.6.1.3 0 .7-.2 1z" fill="#ddd"/></svg><span>+971 50 000 1357</span></div>
    <div class="contact-item"><svg width="14" height="12" viewBox="0 0 14 12"><rect x="1" y="1" width="12" height="10" fill="none" stroke="#ddd" stroke-width="1.4"/><path d="M1 1l6 5 6-5" fill="none" stroke="#ddd" stroke-width="1.4"/></svg><span>info@brightcampuslink.ae</span></div>
  </div>
  <div class="f-col" style="left:846px"><h4>Quick Contact</h4>
    <div class="f-form"><div>Name</div><div>Phone</div><div class="wide">Email</div><div class="wide msg">Message</div></div>
    <div class="f-send">Send</div>
  </div>
</footer>

<div class="bottombar">
  <span class="copy">CopyRight © 2018 BRIGHT CAMPUS . All Right Reserve · Privacy Policy · Terms &amp; Conditions</span>
  <div class="social"><span class="dot"></span><span class="dot"></span><span class="dot"></span><span class="dot"></span><span class="dot"></span><span class="dot"></span></div>
</div>

</body>
</html>
```